Letterhead design of KESTREL POWER THRIFT INC.

we are a energy saving company doing the solar screen, radian barrier, attic insulation, double panel windows. Basically i need the design of the letterhead including my company name, business address, phone numbers, fax number and email address. Main thing i need it look like a huge company and look like very high class. thanks !!

Reason: Please send me more new design about my company! Thanks so much!!

Industry/Entity Type

Business

```html
<!DOCTYPE html>
<html lang="en">
<head>
<meta charset="utf-8">
<title>Kestrel Power Thrift Inc. — Letterhead</title>
<link rel="stylesheet" href="https://fonts.googleapis.com/css2?family=Bebas+Neue&family=Quicksand:wght@300;500;600&display=swap">
<style>
  :root {
    --ink: #000000;
    --gold: #c4962e;
    --paper: #ffffff;
    --thin-ink: #2a2a2a;
  }
  * { margin: 0; padding: 0; box-sizing: border-box; }
  html, body {
    width: 1200px;
    height: 230px;
    overflow: hidden;
    background: var(--paper);
  }
  .letterhead {
    position: relative;
    width: 1200px;
    height: 230px;
    background: var(--paper);
    color: var(--ink);
  }
  .company-name {
    position: absolute;
    left: 2px;
    top: -4px;
    font-family: "Bebas Neue", "Oswald", sans-serif;
    font-size: 78px;
    line-height: 79px;
    letter-spacing: 1px;
    color: var(--ink);
  }
  .company-name span { display: block; white-space: nowrap; }
  .company-name .suffix { color: var(--gold); margin-left: 8px; }

  .contact-list {
    position: absolute;
    right: 12px;
    top: 0;
    list-style: none;
    font-family: "Quicksand", sans-serif;
    font-size: 20px;
    font-weight: 500;
    text-align: right;
    text-transform: uppercase;
  }
  .contact-list li {
    height: 44px;
    line-height: 28px;
    white-space: nowrap;
  }
  .contact-list .label {
    color: var(--gold);
    margin-right: 6px;
  }
  .contact-list .value { color: var(--ink); }

  .address {
    position: absolute;
    right: 2px;
    bottom: 2px;
    font-family: "Quicksand", sans-serif;
    font-size: 28px;
    line-height: 32px;
    text-transform: uppercase;
    white-space: nowrap;
    letter-spacing: 0.5px;
  }
  .address .street,
  .address .postcode { font-weight: 300; color: var(--thin-ink); }
  .address .city { font-weight: 600; color: var(--ink); margin: 0 14px 0 6px; }
</style>
</head>
<body>
  <header class="letterhead">
    <h1 class="company-name">
      <span>Kestrel</span>
      <span>Power</span>
      <span>Thrift<span class="suffix">Inc.</span></span>
    </h1>

    <ul class="contact-list">
      <li><span class="label">Phone:</span><span class="value">555-014-2236</span></li>
      <li><span class="label">Fax:</span><span class="value">555-018-4407</span></li>
      <li><span class="label">Email:</span><span class="value">kestrelpowerthrift@mailbox.com</span></li>
    </ul>

    <p class="address">
      <span class="street">2280 Alder Creek Dr Suite #500</span>
      <span class="city">Brambleton , Texas</span>
      <span class="postcode">77990</span>
    </p>
  </header>
</body>
</html>
```